Promotion of New website mobile app and mobile depsoit

We need a postcard designed to help us promote our New Website, Mobile App and Mobile Deposit. We are based out of Center, Texas and we are a 115 year old Community Bank named Pinecrest Valley Bank. Trying to get all this on one postcard with simple short and sweet message our customer can take home with them. Our new WEB address will be PVBKWX.example our colors are green and white, but different mixes will be fine. I like the slogan Bigger. Bolder. Better. Banking.

Target Market(s)

Bank Customers

Font styles to use
Serif

Requirements
Must have
• PVBKWX.EXAMPLE
• Mobile Deposit
• New App
• Dark Green, Black and white
• Under logo must have member NLRC
Should not have
• Any Blue

```html
<!DOCTYPE html>
<html lang="en">
<head>
<meta charset="utf-8">
<title>Pinecrest Valley Bank Postcard</title>
<link href="https://fonts.googleapis.com/css2?family=Cinzel:wght@400;700&family=Playfair+Display:wght@900&family=Open+Sans:wght@400;600;700&display=swap" rel="stylesheet">
<style>
:root{
  --green:#1c9a48;
  --green-dark:#137a36;
  --green-light:#34b85f;
  --black:#111;
  --white:#fff;
  --grey-light:#f2f2f2;
  --grey-mid:#d4d4d4;
  --page:#e9e9e6;
}
*{box-sizing:border-box;margin:0;padding:0}
html,body{width:1200px;height:857px;overflow:hidden;background:var(--page)}
.canvas{position:relative;width:1200px;height:857px}
.card{position:absolute;top:251px;width:560px;height:354px;overflow:hidden;box-shadow:0 6px 18px rgba(0,0,0,.18)}
.card--back{left:20px;background:var(--white)}
.card--front{left:620px;background:linear-gradient(160deg,var(--white) 0%,var(--grey-light) 45%,var(--grey-mid) 100%)}
.card svg.shapes{position:absolute;inset:0}
.brand{position:absolute;display:flex;align-items:center;gap:8px;font-family:"Playfair Display",serif;font-weight:900;color:var(--black);line-height:1;white-space:nowrap}
.brand__mark{border:2px solid var(--black);flex:none}
.front-brand{left:26px;top:30px;font-size:22px}
.front-brand .brand__mark{width:32px;height:32px}
.back-brand{left:316px;top:36px;font-size:11px;gap:6px}
.back-brand .brand__mark{width:18px;height:18px}
.member-line{position:absolute;left:316px;top:62px;font:600 6px "Open Sans",sans-serif;letter-spacing:.4px;color:var(--black)}
.member-line span{margin-right:14px}
.stamp-box{position:absolute;right:20px;top:18px;width:66px;height:48px;border:1.5px solid var(--black)}
.headline{position:absolute;left:26px;top:118px;font-family:"Cinzel",serif;font-weight:400;font-size:31px;line-height:1.02;color:var(--black)}
.headline .accent{color:var(--green-light)}
.front-copy{position:absolute;left:26px;top:194px;width:300px;font:400 10px/1.35 "Open Sans",sans-serif;color:var(--black)}
.photo{position:absolute;right:0;top:0;width:230px;height:262px;background:radial-gradient(ellipse at 55% 35%,#e4c9a4 0%,#c9ad88 28%,#b8b8bc 52%,#dedede 80%)}
.cta{position:absolute;left:0;right:0;bottom:14px;text-align:center;font-family:"Cinzel",serif;font-weight:400;font-size:15px;letter-spacing:.5px;color:var(--white)}
.panel-title{position:absolute;left:18px;top:22px;font:600 15px "Open Sans",sans-serif;color:var(--white)}
.feature{position:absolute;left:20px;display:flex;align-items:center;gap:18px}
.feature svg{width:44px;height:38px;flex:none}
.feature p{width:190px;font:400 8.5px/1.3 "Open Sans",sans-serif;color:var(--white)}
.feature strong{font-weight:700}
.contact{position:absolute;left:18px;top:286px;font:400 9.5px/1.5 "Open Sans",sans-serif;color:var(--white)}
.store-badges{position:absolute;left:18px;top:320px;display:flex;gap:10px}
.store-badge{width:104px;height:26px;border:1px solid var(--white);border-radius:5px;background:var(--black)}
</style>
</head>
<body>
<main class="canvas">

  <section class="card card--back" aria-label="Postcard back">
    <svg class="shapes" viewBox="0 0 560 354" aria-hidden="true">
      <defs>
        <clipPath id="panelClip"><path d="M0,0 L258,0 Q300,80 304,170 Q308,270 292,354 L0,354Z"/></clipPath>
        <linearGradient id="panelGreen" x1="0" y1="0" x2="0" y2="1">
          <stop offset="0" stop-color="#1c9a48"/><stop offset="1" stop-color="#137a36"/>
        </linearGradient>
      </defs>
      <g clip-path="url(#panelClip)">
        <rect width="560" height="354" fill="url(#panelGreen)"/>
        <rect y="270" width="560" height="84" fill="#111"/>
        <rect y="268" width="560" height="2" fill="#34b85f"/>
      </g>
      <path d="M262,0 Q305,80 309,170 Q313,270 297,354" fill="none" stroke="#111" stroke-width="3"/>
    </svg>
    <h2 class="panel-title">TITLE GOES HERE</h2>
    <div class="feature" style="top:60px">
      <svg viewBox="0 0 44 38" aria-hidden="true"><rect x="3" y="4" width="34" height="22" rx="2" fill="none" stroke="#fff" stroke-width="3"/><rect x="15" y="27" width="10" height="5" fill="#fff"/><rect x="10" y="32" width="20" height="3" fill="#fff"/><circle cx="36" cy="27" r="7" fill="#fff"/></svg>
      <p><strong>New Website:</strong> Lorem ipsum dolor sit amet, consectetuer adipiscing elit, sed diam nonummy nibh euismod</p>
    </div>
    <div class="feature" style="top:118px">
      <svg viewBox="0 0 44 38" aria-hidden="true"><rect x="9" y="2" width="24" height="34" rx="3" fill="none" stroke="#fff" stroke-width="3"/><rect x="14" y="10" width="14" height="2.5" fill="#fff"/><rect x="14" y="16" width="14" height="2.5" fill="#fff"/><rect x="14" y="22" width="9" height="2.5" fill="#fff"/><path d="M28,36 Q34,24 42,30 L42,36Z" fill="#fff"/></svg>
      <p><strong>New App:</strong> Lorem ipsum dolor sit amet, consectetuer adipiscing elit, sed diam nonummy nibh euismod</p>
    </div>
    <div class="feature" style="top:176px">
      <svg viewBox="0 0 44 38" aria-hidden="true"><rect x="5" y="3" width="34" height="30" rx="2" fill="none" stroke="#fff" stroke-width="3"/><circle cx="20" cy="18" r="5" fill="none" stroke="#fff" stroke-width="2.5"/><rect x="30" y="12" width="3" height="12" fill="#fff"/><rect x="9" y="33" width="5" height="3" fill="#fff"/><rect x="30" y="33" width="5" height="3" fill="#fff"/></svg>
      <p><strong>Mobile Deposit:</strong> Lorem ipsum dolor sit amet, consectetuer adipiscing elit, sed diam nonummy nibh</p>
    </div>
    <p class="contact">Call: 123 456 7890 | Mail: info@pvbkwx.example<br>Address Line 1 | Address Line 2</p>
    <div class="store-badges"><span class="store-badge"></span><span class="store-badge"></span></div>

    <div class="brand back-brand"><span class="brand__mark"></span>Pinecrest Valley Bank</div>
    <p class="member-line"><span>MEMBER NLRC</span><span>EQUAL HOUSING LENDER</span></p>
    <div class="stamp-box"></div>
  </section>

  <section class="card card--front" aria-label="Postcard front">
    <div class="photo" role="img" aria-label="Photo of a smiling young woman using a smartphone"></div>
    <svg class="shapes" viewBox="0 0 560 354" aria-hidden="true">
      <defs>
        <linearGradient id="bandGreen" x1="0" y1="0" x2="0" y2="1">
          <stop offset="0" stop-color="#28ad55"/><stop offset="1" stop-color="#137a36"/>
        </linearGradient>
      </defs>
      <path d="M0,300 Q330,292 560,230 L560,354 L0,354Z" fill="url(#bandGreen)"/>
      <path d="M120,290 Q390,282 560,222" fill="none" stroke="#111" stroke-width="3"/>
      <path d="M0,296 Q320,290 560,226" fill="none" stroke="#fff" stroke-width="1.5" opacity=".7"/>
    </svg>
    <div class="brand front-brand"><span class="brand__mark"></span>Pinecrest Valley Bank</div>
    <h1 class="headline">BIGGER.BOLDER.<br>BETTER.<span class="accent">BANKING.</span></h1>
    <p class="front-copy">Lorem ipsum dolor sit amet, consectetuer adipiscing elit, sed diam nonummy nibh euismod tincidunt ut laoreet dolore magna aliquam erat volutpat.</p>
    <p class="cta">For More Information Please Visit www.PVBKWX.example</p>
  </section>

</main>
</body>
</html>
```